Scholarly Pathways - educational consulting

I am beginning an Scholarly Pathways business - focusing on Tribal (Native American Indian) Communities, but will work with anyone. I have work experience in K-12 and Higher Education. Special Education - transition from school to work. Advising and facilitating with academic skills in higher education. I have a BS - Special Education, Masters - Educational Administration and working on a PhD in Higher Education. Also completing PMB approved certification as an Academic Life Coach

Target Market(s)

K12 college bound students and parents, Kinfolk Crossings college bound students and families, special education college bound students and parents

Industry/Entity Type

Business

Contact Information for Business Card

Marnie Odell Fenwick. PO Box 417, Cushing, OK 74023. (918) 555-0293. marnie@scholarlypathways.example

Requirements
Must have
• Scholarly Pathways is the name of the business - Kinfolk Crossings is a focus area
Nice to have
• Tourquoise would be nice. I do not have a logo yet

```html
<!DOCTYPE html>
<html lang="en">
<head>
<meta charset="utf-8">
<title>Scholarly Pathways – Business Card</title>
<link rel="stylesheet" href="https://fonts.googleapis.com/css2?family=Lato:wght@400;700;900&display=swap">
<style>
  :root {
    --backdrop: #3a302b;
    --card: #1b1b1c;
    --card-edge: #111112;
    --ink-light: #f2f2f2;
    --ink-soft: #d9d9d9;
    --accent: #3fb54a;
    --silver: #b9b9bb;
    --rule: #3a3a3c;
  }
  * { margin: 0; padding: 0; box-sizing: border-box; }
  html, body {
    width: 1200px; height: 844px; overflow: hidden;
    background: var(--backdrop);
    font-family: "Lato", Arial, sans-serif;
  }
  .stage {
    position: relative; width: 1200px; height: 844px;
  }
  .card {
    position: absolute; top: 272px;
    width: 520px; height: 300px;
    background: var(--card);
    border: 1px solid var(--card-edge);
    box-shadow: 0 10px 30px rgba(0,0,0,.45);
  }
  .card--front { left: 50px; }
  .card--back { left: 630px; }

  .brand {
    position: absolute; display: flex; align-items: center; gap: 12px;
  }
  .brand__dot {
    width: 34px; height: 34px; border-radius: 50%;
    flex: none;
  }
  .brand__name {
    font-weight: 900; text-transform: uppercase;
    line-height: 1.05; letter-spacing: .5px;
  }
  .card--front .brand { left: 32px; top: 128px; }
  .card--front .brand__dot { background: var(--accent); }
  .card--front .brand__name { color: var(--ink-light); font-size: 19px; }

  .card--back .brand {
    left: 0; right: 0; top: 0; bottom: 0; justify-content: center;
  }
  .card--back .brand__dot { width: 52px; height: 52px; background: var(--silver); }
  .card--back .brand__name { color: var(--silver); font-size: 26px; }

  .divider {
    position: absolute; left: 262px; top: 40px;
    width: 1px; height: 220px; background: var(--rule);
  }
  .contact {
    position: absolute; left: 280px; top: 44px; right: 16px;
    color: var(--ink-soft); font-size: 13.5px; line-height: 1.35;
  }
  .contact__name { color: var(--ink-light); font-size: 20px; font-weight: 400; }
  .contact__title { color: var(--accent); font-size: 13.5px; margin-bottom: 16px; }
  .contact__address { margin-bottom: 14px; }
  .contact__line { white-space: nowrap; }
  .contact__label { color: var(--accent); display: inline-block; width: 16px; }
</style>
</head>
<body>
<main class="stage">
  <section class="card card--front" aria-label="Business card front">
    <div class="brand">
      <span class="brand__dot"></span>
      <span class="brand__name">Scholarly<br>Pathways</span>
    </div>
    <div class="divider"></div>
    <div class="contact">
      <p class="contact__name">Marnie Odell Fenwick</p>
      <p class="contact__title">Managing Director</p>
      <p class="contact__address">PO Box 417,<br>Cushing, OK 74023</p>
      <p class="contact__line"><span class="contact__label">T:</span> (918) 555-0293</p>
      <p class="contact__line"><span class="contact__label">E:</span> marnie@scholarlypathways.example</p>
      <p class="contact__line"><span class="contact__label">W:</span> www.scholarlypathways.example</p>
    </div>
  </section>

  <section class="card card--back" aria-label="Business card back">
    <div class="brand">
      <span class="brand__dot"></span>
      <span class="brand__name">Scholarly<br>Pathways</span>
    </div>
  </section>
</main>
</body>
</html>
```